Business card for home decor store and design

I need a business card for my home decor boutique that’s professional looking boho/rustic. We sell vintage furniture, vintage finds, lamps, throws, rugs. We also carry a Diy paint line for refinishing furniture. We offer workshop on painting furniture, private or group setting. We in the heart of Old Town Red Bluff. We love to design, build and restore. Family owned small business. Our style is rustic boho farmhouse. We search for one of a kind found and repurposed items. We love vintage home decor, vintage windows.

Target Market(s)

Home decor

Industry/Entity Type

Home Accessories

Contact Information for Business Card

Have a rustic look/boho

Font styles to use
Serif
Script

Requirements
Must have
• Logo

```html
<!DOCTYPE html>
<html lang="en">
<head>
<meta charset="utf-8">
<title>Birch &amp; Loom Co. — Business Card</title>
<link rel="stylesheet" href="https://fonts.googleapis.com/css2?family=Roboto:wght@400;700&display=swap">
<style>
  :root {
    --backdrop: #6b6b6b;
    --ink: #0d0d0d;
    --paper: #ffffff;
    --muted: #2a2a2a;
    --rule: #222222;
  }
  html, body {
    margin: 0;
    padding: 0;
    width: 1200px;
    height: 1124px;
    overflow: hidden;
    background: var(--backdrop);
    font-family: "Roboto", Arial, sans-serif;
  }
  .sheet {
    position: relative;
    width: 1200px;
    height: 1124px;
  }
  .card {
    position: absolute;
    left: 145px;
    width: 910px;
    height: 520px;
    box-shadow: 0 8px 22px rgba(0,0,0,0.35);
    overflow: hidden;
  }
  .card--front {
    top: 30px;
    background: var(--ink);
  }
  .card--back {
    top: 574px;
    background: var(--paper);
  }
  .front__stars {
    position: absolute;
    inset: 0;
    width: 910px;
    height: 520px;
  }
  .front__stripe {
    position: absolute;
    left: 0;
    right: 0;
    bottom: 10px;
    height: 14px;
    background: var(--paper);
  }
  .brand {
    position: absolute;
    display: flex;
    align-items: center;
    gap: 16px;
    font-family: "Roboto", Arial, sans-serif;
    font-weight: 700;
    white-space: nowrap;
  }
  .brand__dot {
    border-radius: 50%;
    flex: none;
  }
  .card--front .brand {
    left: 50%;
    top: 240px;
    transform: translateX(-50%);
    color: var(--paper);
    font-size: 46px;
  }
  .card--front .brand__dot { width: 30px; height: 30px; background: var(--paper); }
  .card--back .brand {
    left: 60px;
    top: 234px;
    color: var(--ink);
    font-size: 34px;
  }
  .card--back .brand__dot { width: 24px; height: 24px; background: var(--ink); }
  .divider {
    position: absolute;
    left: 455px;
    top: 95px;
    width: 2px;
    height: 330px;
    background: var(--rule);
  }
  .contact {
    position: absolute;
    left: 495px;
    top: 108px;
    color: var(--muted);
  }
  .contact__name {
    margin: 0;
    font-size: 34px;
    font-weight: 700;
    color: var(--ink);
  }
  .contact__role {
    margin: 4px 0 0;
    font-size: 27px;
  }
  .contact__address {
    margin: 28px 0 0;
    font-size: 25px;
    line-height: 1.25;
  }
  .contact__list {
    list-style: none;
    margin: 30px 0 0;
    padding: 0;
    font-size: 26px;
  }
  .contact__list li {
    display: flex;
    align-items: center;
    gap: 18px;
    margin-bottom: 8px;
  }
  .contact__icon {
    width: 20px;
    height: 20px;
    flex: none;
  }
</style>
</head>
<body>
<main class="sheet">
  <section class="card card--front" aria-label="Card front">
    <svg class="front__stars" viewBox="0 0 910 520" aria-hidden="true">
      <defs>
        <path id="star" d="M0,-10 L2.35,-3.24 L9.51,-3.09 L3.8,1.24 L5.88,8.09 L0,4 L-5.88,8.09 L-3.8,1.24 L-9.51,-3.09 L-2.35,-3.24 Z" fill="#fff"/>
      </defs>
      <use href="#star" transform="translate(640 70) scale(0.5)"/>
      <use href="#star" transform="translate(790 45) scale(0.55)"/>
      <use href="#star" transform="translate(805 135) scale(0.5)"/>
      <use href="#star" transform="translate(875 185) scale(1.1)"/>
      <use href="#star" transform="translate(780 225) scale(0.75)"/>
      <use href="#star" transform="translate(255 200) scale(0.5)"/>
      <use href="#star" transform="translate(115 345) scale(0.45)"/>
      <use href="#star" transform="translate(225 405) scale(0.6)"/>
      <use href="#star" transform="translate(395 415) scale(0.75)"/>
      <use href="#star" transform="translate(230 490) scale(1.1)"/>
    </svg>
    <div class="brand"><span class="brand__dot"></span><span>Birch &amp; Loom Co.</span></div>
    <div class="front__stripe"></div>
  </section>

  <section class="card card--back" aria-label="Card back">
    <div class="brand"><span class="brand__dot"></span><span>Birch &amp; Loom Co.</span></div>
    <div class="divider"></div>
    <div class="contact">
      <h1 class="contact__name">Daniel Reyes</h1>
      <p class="contact__role">Manager</p>
      <p class="contact__address">Your address, city<br>state, ZIP 0000</p>
      <ul class="contact__list">
        <li>
          <svg class="contact__icon" viewBox="0 0 24 24" aria-hidden="true"><path fill="#222" d="M6.6 10.8a15 15 0 0 0 6.6 6.6l2.2-2.2a1 1 0 0 1 1-.25 11.4 11.4 0 0 0 3.6.57 1 1 0 0 1 1 1V20a1 1 0 0 1-1 1A17 17 0 0 1 3 4a1 1 0 0 1 1-1h3.5a1 1 0 0 1 1 1c0 1.250.2 2.450.57 3.57a1 1 0 0 1-.25 1z"/></svg>
          <span>555-014-2100</span>
        </li>
        <li>
          <svg class="contact__icon" viewBox="0 0 24 24" aria-hidden="true"><rect x="2.5" y="5" width="19" height="14" rx="1.5" fill="none" stroke="#222" stroke-width="2"/><path d="M3 6l9 7 9-7" fill="none" stroke="#222" stroke-width="2"/></svg>
          <span>hello@birchloom.com</span>
        </li>
        <li>
          <svg class="contact__icon" viewBox="0 0 24 24" aria-hidden="true"><circle cx="12" cy="12" r="9.5" fill="none" stroke="#222" stroke-width="2"/><ellipse cx="12" cy="12" rx="4" ry="9.5" fill="none" stroke="#222" stroke-width="2"/><path d="M2.5 12h19M4 7h16M4 17h16" stroke="#222" stroke-width="1.6"/></svg>
          <span>www.birchloom.com</span>
        </li>
      </ul>
    </div>
  </section>
</main>
</body>
</html>
```